Wine Label for a Sweet Wine Called "Glimmo"

We need a wine label that will be used for both a sweet red and a sweet white wine. The very important thing to remember is the target market for these wines is: young American women who love sweet wines and they also spend a lot of their money on their hair, clothes, jewelry, nails. They LOVE Glimmo (Glimmo is a word used to describe flashy accessories, jewelry, decoration.) This label needs to be eye catching, showy, fun, glittery. Please put the brand name, "Glimmo," big, and then in smaller but still readable words underneath the label or somewhere on the label: Sweet, Sophisticated, Red (or white). (An example of what I mean is attached). To differentiate between the two color wines you can suggest color changes to differentiate between the red label and the white label but the label design itself should be the same. Ultimately, the label can be the exact same label for both white and red as long as it looks good on a white wine (a greenish/yellow wine in a clear glass bottle) and a red wine (a dark color wine in a dark bottle).

I've attached an example of the text size relationship between the word Glimmo and the words to go underneath or elsewhere on the label, but you can certainly play with this-- it is just a suggestion of the text size relationship, and definitely NOT at all mandatory that you use any of these fonts.

You can pick the size of the label but try to stay within normal wine label sizes, meaning don't go bigger than approx. 3.5 inches wide and 5 inches tall.

Target Market(s)

Young American women who love sweet wines and spend a lot of money on their hair, clothes, jewelry, nails. They love Glimmo (Glimmo is a word that means flashy accessories, jewelry, decoration)

Requirements
Must have
• It needs to be flashy, glittery, fun, eye catching, memorable
Nice to have
• It shouldn't be too too ultra feminine! The target market is strong independent women and we also have men who will buy it too.

```html
<!DOCTYPE html>
<html lang="en">
<head>
<meta charset="utf-8">
<title>Glimmo – Sweet Wine Labels</title>
<link rel="stylesheet" href="https://fonts.googleapis.com/css2?family=Abril+Fatface&family=Montserrat:wght@400&display=swap">
<style>
  :root {
    --canvas-light: #ffffff;
    --canvas-edge: #dcdcdc;
    --red-deep: #4e1619;
    --red-mid: #7d3a3b;
    --red-rose: #a56a66;
    --red-glow: #e9d3cc;
    --red-frame: #7a2a2c;
    --red-text: #f1e2de;
    --white-deep: #d9a23a;
    --white-mid: #efc968;
    --white-glow: #fff8e2;
    --white-frame: #ecd29a;
    --white-text: #7d4a36;
    --frame-line: #ffffff;
    --sparkle: #ffffff;
  }
  * { margin: 0; padding: 0; box-sizing: border-box; }
  html, body { width: 1200px; height: 1000px; overflow: hidden; }
  body {
    background: radial-gradient(ellipse at 50% 45%, var(--canvas-light) 0%, #f2f2f2 55%, var(--canvas-edge) 100%);
    display: flex;
    align-items: center;
    justify-content: center;
    gap: 120px;
  }
  .label {
    position: relative;
    width: 340px;
    height: 493px;
  }
  .label__art { position: absolute; inset: 0; width: 100%; height: 100%; }
  .label__text {
    position: absolute;
    left: 0; right: 0;
    top: 54%;
    text-align: center;
  }
  .label__brand {
    font-family: "Abril Fatface", "Playfair Display", serif;
    font-size: 56px;
    line-height: 1;
    letter-spacing: 0.5px;
  }
  .label__tagline {
    margin-top: 8px;
    font-family: "Montserrat", Arial, sans-serif;
    font-size: 8.5px;
    letter-spacing: 2.2px;
    text-transform: uppercase;
  }
  .label--red .label__brand, .label--red .label__tagline { color: var(--red-text); }
  .label--white .label__brand, .label--white .label__tagline { color: var(--white-text); }
</style>
</head>
<body>

  <div class="label label--red">
    <svg class="label__art" viewBox="0 0 255 370">
      <defs>
        <clipPath id="redShape">
          <path d="M14,0 H241 A14,14 0 0 0 255,14 V356 A14,14 0 0 0 241,370 H14 A14,14 0 0 0 0,356 V14 A14,14 0 0 0 14,0 Z"/>
        </clipPath>
        <linearGradient id="redBase" x1="0" y1="0" x2="1" y2="1">
          <stop offset="0%" stop-color="var(--red-mid)"/>
          <stop offset="50%" stop-color="var(--red-rose)"/>
          <stop offset="100%" stop-color="var(--red-deep)"/>
        </linearGradient>
        <radialGradient id="redGlow">
          <stop offset="0%" stop-color="var(--red-glow)" stop-opacity="0.9"/>
          <stop offset="100%" stop-color="var(--red-glow)" stop-opacity="0"/>
        </radialGradient>
        <linearGradient id="redStreak" x1="0" y1="0" x2="1" y2="0">
          <stop offset="0%" stop-color="var(--sparkle)" stop-opacity="0"/>
          <stop offset="50%" stop-color="var(--sparkle)" stop-opacity="0.45"/>
          <stop offset="100%" stop-color="var(--sparkle)" stop-opacity="0"/>
        </linearGradient>
      </defs>
      <g role="img" aria-label="Glittering bokeh sparkle background in deep wine red with diagonal light streaks" clip-path="url(#redShape)">
        <rect width="255" height="370" fill="url(#redBase)"/>
        <ellipse cx="70" cy="80" rx="90" ry="70" fill="url(#redGlow)"/>
        <ellipse cx="200" cy="50" rx="70" ry="55" fill="url(#redGlow)" opacity="0.7"/>
        <ellipse cx="150" cy="250" rx="110" ry="60" fill="url(#redGlow)" opacity="0.6"/>
        <ellipse cx="40" cy="330" rx="70" ry="50" fill="url(#redGlow)" opacity="0.5"/>
        <g transform="rotate(28 127 185)">
          <rect x="-60" y="60" width="380" height="22" fill="url(#redStreak)"/>
          <rect x="-60" y="100" width="380" height="10" fill="url(#redStreak)"/>
          <rect x="-60" y="30" width="380" height="8" fill="url(#redStreak)"/>
        </g>
      </g>
      <path d="M14,0 H241 A14,14 0 0 0 255,14 V356 A14,14 0 0 0 241,370 H14 A14,14 0 0 0 0,356 V14 A14,14 0 0 0 14,0 Z"
            fill="none" stroke="var(--red-frame)" stroke-width="3"/>
      <path d="M20,7 H235 A13,13 0 0 0 248,20 V350 A13,13 0 0 0 235,363 H20 A13,13 0 0 0 7,350 V20 A13,13 0 0 0 20,7 Z"
            fill="none" stroke="var(--frame-line)" stroke-width="1.6" opacity="0.9"/>
    </svg>
    <div class="label__text">
      <div class="label__brand">Glimmo</div>
      <div class="label__tagline">Sweet | Red | Sophisticated</div>
    </div>
  </div>

  <div class="label label--white">
    <svg class="label__art" viewBox="0 0 255 370">
      <defs>
        <clipPath id="goldShape">
          <path d="M14,0 H241 A14,14 0 0 0 255,14 V356 A14,14 0 0 0 241,370 H14 A14,14 0 0 0 0,356 V14 A14,14 0 0 0 14,0 Z"/>
        </clipPath>
        <linearGradient id="goldBase" x1="0" y1="0" x2="1" y2="1">
          <stop offset="0%" stop-color="var(--white-mid)"/>
          <stop offset="55%" stop-color="var(--white-deep)"/>
          <stop offset="100%" stop-color="var(--white-mid)"/>
        </linearGradient>
        <radialGradient id="goldGlow">
          <stop offset="0%" stop-color="var(--white-glow)" stop-opacity="1"/>
          <stop offset="100%" stop-color="var(--white-glow)" stop-opacity="0"/>
        </radialGradient>
        <linearGradient id="goldStreak" x1="0" y1="0" x2="1" y2="0">
          <stop offset="0%" stop-color="var(--sparkle)" stop-opacity="0"/>
          <stop offset="50%" stop-color="var(--sparkle)" stop-opacity="0.55"/>
          <stop offset="100%" stop-color="var(--sparkle)" stop-opacity="0"/>
        </linearGradient>
      </defs>
      <g role="img" aria-label="Glittering bokeh sparkle background in golden champagne tones with diagonal light streaks" clip-path="url(#goldShape)">
        <rect width="255" height="370" fill="url(#goldBase)"/>
        <ellipse cx="60" cy="70" rx="90" ry="70" fill="url(#goldGlow)"/>
        <ellipse cx="210" cy="200" rx="70" ry="90" fill="url(#goldGlow)" opacity="0.8"/>
        <ellipse cx="110" cy="250" rx="100" ry="60" fill="url(#goldGlow)" opacity="0.7"/>
        <ellipse cx="200" cy="340" rx="80" ry="50" fill="url(#goldGlow)" opacity="0.6"/>
        <g transform="rotate(28 127 185)">
          <rect x="-60" y="60" width="380" height="22" fill="url(#goldStreak)"/>
          <rect x="-60" y="100" width="380" height="10" fill="url(#goldStreak)"/>
          <rect x="-60" y="30" width="380" height="8" fill="url(#goldStreak)"/>
        </g>
      </g>
      <path d="M14,0 H241 A14,14 0 0 0 255,14 V356 A14,14 0 0 0 241,370 H14 A14,14 0 0 0 0,356 V14 A14,14 0 0 0 14,0 Z"
            fill="none" stroke="var(--white-frame)" stroke-width="3"/>
      <path d="M20,7 H235 A13,13 0 0 0 248,20 V350 A13,13 0 0 0 235,363 H20 A13,13 0 0 0 7,350 V20 A13,13 0 0 0 20,7 Z"
            fill="none" stroke="var(--frame-line)" stroke-width="1.6" opacity="0.9"/>
    </svg>
    <div class="label__text">
      <div class="label__brand">Glimmo</div>
      <div class="label__tagline">Sweet | White | Sophisticated</div>
    </div>
  </div>

</body>
</html>
```